Fresh Nest Builder Guide needs a new Landing Page

I like to get a landing page or website with 2-3 pages to help target home buyers who are looking to buy homes from builders such as PV Dwellings, Moritz, G.T. Falwick, etc. The landing page/website to be non-cluttered and be able to explain to home buyers that there are many benefits to include me as their buyer's agent when they buy a brand new home from any builders.
I may want to incorporate a short explanation video (animated) on the landing page and then for the viewer to click on a button that will take them to another page where they can search for new homes from different builders.
Target Market(s)
Home buyers looking to buy brand new home from builders such as PV Dwellings, Moritz, G.T. Falwick, etc.
Industry/Entity Type
Real Estate
Number of Pages Required
2 page
Requirements
Must have
- The landing page may have the explanation video at the bottom of the landing page (scrolled down) or there may be a CALL TO ACTION button that takes the viewer to the 2nd page to watch the explanation video. Once they watched the explanation video and are still interested, they can click on another CALL TO ACTION button that will take them to another website that they will be able to search for all the available new homes and register their contact information.
Should not have
- No clutters and no dark colors.

```html
<!DOCTYPE html>
<html lang="en">
<head>
<meta charset="utf-8">
<title>Blockwise Home Visit</title>
<link rel="stylesheet" href="https://fonts.googleapis.com/css2?family=Raleway:wght@400;500;600;700;800&display=swap">
<style>
  :root {
    --orange: #ee8c2f;
    --green: #a3b838;
    --heading-green: #a6b535;
    --teal: #1f7d86;
    --blue: #6fa3d5;
    --ink: #3a3a3a;
    --body: #555;
    --white: #fff;
  }
  * { box-sizing: border-box; margin: 0; padding: 0; }
  html, body { width: 1083px; height: 1200px; overflow: hidden; }
  body { position: relative; background: var(--white); font-family: 'Raleway', sans-serif; color: var(--ink); }

  .site-header { position: absolute; left: 0; top: 0; width: 1083px; height: 67px; background: var(--white); }
  .brand { position: absolute; left: 170px; top: 22px; display: flex; align-items: center; gap: 8px; font-size: 17px; font-weight: 600; color: #3b2a1e; }
  .brand-dot { width: 14px; height: 14px; border-radius: 50%; background: var(--green); }
  .main-nav { position: absolute; top: 27px; font-size: 10.5px; font-weight: 500; letter-spacing: .2px; color: #444; }
  .main-nav a { position: absolute; color: inherit; text-decoration: none; white-space: nowrap; }
  .btn { position: absolute; display: flex; align-items: center; justify-content: center; color: var(--white); font-weight: 600; font-size: 10.5px; letter-spacing: .2px; border-radius: 2px; text-decoration: none; }
  .btn-quote { left: 765px; top: 18px; width: 149px; height: 31px; background: var(--orange); }

  .hero { position: absolute; left: 0; top: 67px; width: 1083px; height: 457px;
    background: linear-gradient(100deg, #8f7a68 0%, #c9b7a2 28%, #e8ded2 50%, #dccab2 72%, #b98f62 100%); }
  .hero-title { position: absolute; left: 168px; top: 222px; font-size: 29px; line-height: 36px; font-weight: 800; color: var(--white); text-shadow: 0 1px 3px rgba(0,0,0,.25); }
  .btn-tutorial { left: 169px; top: 311px; width: 149px; height: 35px; background: var(--orange); gap: 7px; }
  .scroll-cue { position: absolute; left: 534px; top: 389px; }

  .how-it-works-bg { position: absolute; left: 740px; top: 545px; width: 340px; height: 320px;
    background: radial-gradient(ellipse at center, rgba(200,200,200,.18) 0%, rgba(255,255,255,0) 70%); }
  .side-label-line { position: absolute; left: 151px; top: 577px; width: 1.5px; height: 35px; background: var(--teal); }
  .side-label { position: absolute; left: 145px; top: 734px; transform: rotate(-90deg); transform-origin: left top; font-size: 11px; letter-spacing: 2.6px; color: var(--teal); font-weight: 500; white-space: nowrap; }
  .video-frame { position: absolute; left: 171px; top: 577px; width: 431px; height: 282px; border-radius: 2px; box-shadow: 0 8px 18px rgba(0,0,0,.18);
    background: linear-gradient(180deg, #fbe3ae 0%, #e9c2a6 40%, #c4b79e 62%, #5e5e5e 78%, #9a9a9a 90%, #3d8a3e 100%); }
  .play-btn { position: absolute; left: 365px; top: 697px; }
  .section-title { position: absolute; left: 636px; top: 586px; font-size: 19px; font-weight: 700; letter-spacing: 4px; color: var(--heading-green); }
  .section-copy { position: absolute; left: 636px; width: 282px; font-size: 11.3px; line-height: 17.6px; color: var(--body); }
  .copy-one { top: 627px; }
  .copy-two { top: 708px; }
  .btn-search-homes { left: 636px; top: 811px; width: 182px; height: 35px; background: var(--green); }

  .search-band { position: absolute; left: 0; top: 913px; width: 1083px; height: 246px; background: var(--orange); text-align: center; color: var(--white); }
  .band-notch { position: absolute; left: 526px; top: 900px; }
  .band-title { position: absolute; left: 0; right: 0; top: 49px; font-size: 19px; font-weight: 600; }
  .band-copy { position: absolute; left: 0; right: 0; top: 76px; font-size: 11.5px; line-height: 17.6px; }
  .search-form { position: absolute; left: 290px; top: 132px; width: 503px; height: 36px; background: var(--white); border-radius: 2px; }
  .search-field { position: absolute; left: 21px; top: 11px; font-size: 11.3px; color: #555; }
  .search-btn { position: absolute; left: 405px; top: 3px; width: 95px; height: 30px; background: var(--blue); color: var(--white); font-size: 11.5px; display: flex; align-items: center; justify-content: center; border-radius: 1px; }

  .site-footer { position: absolute; left: 0; top: 1159px; width: 1083px; height: 41px; font-size: 10.5px; color: #444; }
  .copyright { position: absolute; left: 170px; top: 13px; }
  .legal { position: absolute; right: 169px; top: 13px; }
</style>
</head>
<body>
  <header class="site-header">
    <div class="brand"><span class="brand-dot"></span>Blockwise Home Visit</div>
    <nav class="main-nav">
      <a style="left:381px">FIND A HOME</a>
      <a style="left:469px">ABOUT US</a>
      <a style="left:543px">SERVICES</a>
      <a style="left:614px">CONTACT</a>
    </nav>
    <a class="btn btn-quote">REQUEST FREE QUOTE</a>
  </header>

  <section class="hero" role="img" aria-label="Happy couple celebrating in a bright new home among moving boxes">
    <h1 class="hero-title">FINDING YOUR BEST LIVING<br>HOUSE IS OUR MISSION</h1>
    <a class="btn btn-tutorial">
      <svg width="8" height="9" viewBox="0 0 8 9"><path d="M0 0 L8 4.5 L0 9Z" fill="#fff"/></svg>WATCH TUTORIAL</a>
    <svg class="scroll-cue" width="16" height="70" viewBox="0 0 16 70">
      <rect x="1" y="1" width="14" height="24" rx="7" fill="none" stroke="#fff" stroke-width="1.4"/>
      <line x1="8" y1="5" x2="8" y2="10" stroke="#fff" stroke-width="1.4"/>
      <line x1="8" y1="41" x2="8" y2="58" stroke="#fff" stroke-width="1.4"/>
    </svg>
  </section>

  <div class="how-it-works-bg" role="img" aria-label="Faint house blueprint sketch"></div>
  <div class="side-label-line"></div>
  <div class="side-label">VIDEO TUTORIAL</div>
  <div class="video-frame" role="img" aria-label="Animated explainer video still of a town street with a school and bus"></div>
  <svg class="play-btn" width="40" height="40" viewBox="0 0 40 40">
    <circle cx="20" cy="20" r="20" fill="rgba(60,60,60,.55)"/>
    <path d="M15 11 L29 20 L15 29Z" fill="#fff"/>
  </svg>
  <h2 class="section-title">HOW IT WORKS ?</h2>
  <p class="section-copy copy-one">Tempor incididunt ut labore et dolore magna aliqua. Ut enim ad minim veniam, quis nostrud exercitation ullamco laboris nisi ut aliquip ex ea commodo consequat.</p>
  <p class="section-copy copy-two">Duis aute irure dolor in reprehenderit in voluptate velit esse cillum dolore eu fugiat nulla pariatur. Excepteur sint occaecat cupidatat non proident, sunt in culpa qui officia deserunt mollit anim id est laborum. Sed ut perspiciatis unde omnis iste</p>
  <a class="btn btn-search-homes">SEARCH AVAILABLE HOMES</a>

  <section class="search-band">
    <h2 class="band-title">SEARCH FOR A NEW HOME</h2>
    <p class="band-copy">Consectetur adipisicing elit, sed do eiusmod tempor incididunt ut labore et dolore<br>magna aliqua. Ut enim ad minim veniam, quis nostrud exercitation ullamco laboris</p>
    <div class="search-form">
      <span class="search-field">Enter an addressn neighborhood, city or ZIP code.</span>
      <span class="search-btn">Search</span>
    </div>
  </section>
  <svg class="band-notch" width="32" height="30" viewBox="0 0 32 30">
    <path d="M0 13 L32 13 L16 28Z" fill="#fff"/>
    <line x1="16" y1="2" x2="16" y2="12" stroke="#ee8c2f" stroke-width="1.3"/>
    <path d="M12 8.5 L16 12.5 L20 8.5" fill="none" stroke="#ee8c2f" stroke-width="1.3"/>
  </svg>

  <footer class="site-footer">
    <span class="copyright">© 2018 Blockwise Home Visit</span>
    <span class="legal">Privacy Policy &nbsp;|&nbsp; Terms of use</span>
  </footer>
</body>
</html>
```